K&M Trailer Rental promo Flyer 5.5x8.5" Flyer

All assets and several pictures of my trailers, that we rent out, are attached.

Flyer dimensions are 5.5"x8.5" - I'll be having it printed on glossy stock.
The dimensions and capacity of the trailers is key.
Include phone number: 248-555-0186 and our website kandmtrailer-example.com

I want something that will really "POP".

Target Market(s)

Blue collar business owners. Recreational offer roads/4x4 folks, used car dealers, contractors/small business owners. Folks with only occasional need for a trailer

Industry/Entity Type

Trailer Rental

Font styles to use
Other font styles liked:
• Designer's choice/no preference

Colors
EE7325
F08F49
F5BC92
FAE3D3
FDF4ED

Requirements
Must have
• Phone number, website, and details about our trailer offerings

```html
<!DOCTYPE html>
<html lang="en">
<head>
<meta charset="utf-8">
<title>K&amp;M Trailer Rental Flyer</title>
<link rel="stylesheet" href="https://fonts.googleapis.com/css2?family=Montserrat:wght@300;400&family=Roboto+Condensed:wght@300;400;700&display=swap">
<style>
  :root {
    --orange: #ee7325;
    --orange-light: #f08f49;
    --peach: #f5bc92;
    --cream: #fdf4ed;
    --ink: #1c1c1c;
    --paper: #ffffff;
    --backdrop: #ebe8e4;
  }
  * { margin: 0; padding: 0; box-sizing: border-box; }
  html, body { width: 888px; height: 1200px; overflow: hidden; background: var(--backdrop); }
  .flyer {
    position: absolute; left: 74px; top: 30px; width: 740px; height: 1140px;
    background: var(--paper); overflow: hidden;
    font-family: "Roboto Condensed", sans-serif; color: var(--ink);
  }
  .brand-mark {
    position: absolute; left: 118px; top: 30px; width: 78px; height: 78px;
    border-radius: 50%; background: var(--orange);
  }
  .brand-name {
    position: absolute; left: 29px; top: 113px; width: 270px;
    font-weight: 700; font-size: 33px; line-height: 40px; letter-spacing: -0.6px; color: var(--ink);
    white-space: nowrap;
  }
  .call-label {
    position: absolute; left: 428px; top: 79px;
    font-size: 20px; font-weight: 300; letter-spacing: .3px; line-height: 22px;
  }
  .call-number {
    position: absolute; left: 380px; top: 100px;
    display: flex; align-items: center; gap: 4px;
    font-family: "Montserrat", sans-serif; font-weight: 400; font-size: 44px; line-height: 48px;
    color: var(--orange); letter-spacing: .5px; white-space: nowrap;
  }
  .call-number svg { width: 40px; height: 40px; flex: none; }
  .hero {
    position: absolute; left: 0; top: 168px; width: 743px; height: 389px;
    background: linear-gradient(180deg, #9fc6ea 0%, #c9dcea 35%, #6f8a5a 55%, #8d8a7e 72%, #c9b9a0 100%);
  }
  .hero-tag {
    position: absolute; left: 135px; top: 436px; width: 490px; height: 60px;
    background: var(--orange); border-radius: 24px;
    color: #fff; font-size: 29px; text-align: center; line-height: 60px; white-space: nowrap;
  }
  .about-title {
    position: absolute; left: 29px; top: 580px;
    font-weight: 700; font-size: 44px; line-height: 50px; letter-spacing: -.3px; white-space: nowrap;
  }
  .about-title .accent { color: var(--orange); }
  .about-text {
    position: absolute; left: 29px; top: 643px; width: 705px;
    font-weight: 300; font-size: 26px; line-height: 38px;
  }
  .trailer { position: absolute; width: 236px; }
  .trailer-photo { width: 236px; height: 150px; }
  .trailer-equipment { left: 29px; top: 790px; }
  .trailer-equipment .trailer-photo { background: linear-gradient(180deg, #8d8f8e 0%, #a5a6a3 40%, #d6b98a 70%, #8f908e 100%); }
  .trailer-car { left: 279px; top: 793px; }
  .trailer-car .trailer-photo { background: linear-gradient(180deg, #b9cde0 0%, #3e4246 35%, #2c2f33 70%, #3a3d40 100%); }
  .trailer-caption { margin: 7px 0 0 7px; font-size: 21.5px; line-height: 26px; white-space: nowrap; }
  .perks { position: absolute; left: 527px; top: 808px; list-style: none; }
  .perks li { display: flex; align-items: center; gap: 6px; font-size: 20px; height: 38px; white-space: nowrap; }
  .perks svg { width: 22px; height: 22px; flex: none; }
  .footer-wave { position: absolute; left: 0; top: 1010px; width: 740px; height: 130px; }
  .rv-photo {
    position: absolute; left: 523px; top: 996px; width: 218px; height: 91px;
    background: radial-gradient(ellipse at 45% 40%, #e4e5e1 0%, #cfd0cb 55%, rgba(207,208,203,0) 78%);
  }
  .site {
    position: absolute; left: 189px; top: 1086px;
    display: flex; align-items: center; gap: 18px;
    color: #fff; font-size: 29px; line-height: 36px; white-space: nowrap;
  }
  .site svg { width: 26px; height: 26px; flex: none; }
</style>
</head>
<body>
<main class="flyer">
  <div class="brand-mark" aria-hidden="true"></div>
  <div class="brand-name">K&amp;M TRAILER RENTAL</div>

  <div class="call-label">CALL US TODAY</div>
  <div class="call-number">
    <svg viewBox="0 0 40 40" aria-hidden="true"><circle cx="20" cy="20" r="17" fill="none" stroke="currentColor" stroke-width="3"/><path d="M14 11c2-1 3 0 4 3l-2 3c1 3 3 5 6 7l3-2c3 1 4 2 3 4-1 2-3 3-5 2-7-3-11-8-12-14 0-1 1-2 3-3z" fill="currentColor"/></svg>
    <span>248.555.0186</span>
  </div>

  <div class="hero" role="img" aria-label="Photo of a long flatbed trailer carrying two classic cars, hitched to an SUV in front of a white house"></div>
  <div class="hero-tag">CAR / EQUIPMENT TRAILER RENTALS</div>

  <h1 class="about-title"><span class="accent">ABOUT K&amp;M</span> TRAILER RENTAL</h1>
  <p class="about-text">Serving the local community &amp; surrounding areas, we specialize in offering a diverse selection of trailers designed to meet a variety of hauling &amp; transportation needs.</p>

  <figure class="trailer trailer-equipment">
    <div class="trailer-photo" role="img" aria-label="Photo of a long black equipment trailer with a wooden deck in a parking lot"></div>
    <figcaption class="trailer-caption">Ridgeline 30' x 7' 14k lbs<br>Equipment Trailer</figcaption>
  </figure>
  <figure class="trailer trailer-car">
    <div class="trailer-photo" role="img" aria-label="Photo of a black car hauler trailer in a parking lot"></div>
    <figcaption class="trailer-caption">MX 20' X 7' Car Hauler<br>Car Trailer</figcaption>
  </figure>

  <ul class="perks">
    <li><svg viewBox="0 0 22 22" aria-hidden="true"><circle cx="10" cy="12" r="8" fill="none" stroke="#888" stroke-width="1.6"/><path d="M6 12l3 4 9-13" fill="none" stroke="var(--orange)" stroke-width="2.6" stroke-linecap="round"/></svg>Online Booking</li>
    <li><svg viewBox="0 0 22 22" aria-hidden="true"><circle cx="10" cy="12" r="8" fill="none" stroke="#888" stroke-width="1.6"/><path d="M6 12l3 4 9-13" fill="none" stroke="var(--orange)" stroke-width="2.6" stroke-linecap="round"/></svg>Transparency Policy</li>
    <li><svg viewBox="0 0 22 22" aria-hidden="true"><circle cx="10" cy="12" r="8" fill="none" stroke="#888" stroke-width="1.6"/><path d="M6 12l3 4 9-13" fill="none" stroke="var(--orange)" stroke-width="2.6" stroke-linecap="round"/></svg>Top Rated</li>
  </ul>

  <svg class="footer-wave" viewBox="0 0 740 130" preserveAspectRatio="none" aria-hidden="true">
    <path d="M0 118 Q370 -26 740 118 L740 112 Q370 -14 0 112 Z" fill="var(--ink)"/>
    <path d="M0 130 L0 120 Q370 8 740 120 L740 130 Z" fill="var(--orange)"/>
  </svg>
  <div class="rv-photo" role="img" aria-label="Photo of a vintage motorhome loaded on a flatbed trailer"></div>

  <div class="site">
    <svg viewBox="0 0 26 26" aria-hidden="true" fill="none" stroke="#fff" stroke-width="1.5"><circle cx="13" cy="13" r="11"/><ellipse cx="13" cy="13" rx="5" ry="11"/><path d="M2 13h22M4 7h18M4 19h18"/></svg>
    <span>https://kandmtrailer-example.com/</span>
  </div>
</main>
</body>
</html>
```